Need a stunning looking Business Card Design for my Telecom Business, Wow FACTOR!

I deal with high level IT Directors , and Contractors.
I need to impress them with a sleek , professional and unique business card.
Im thinking options as far as rounded edges, plastic , or even metal card or die cut on a corner.
Whatever looks better and leave an unforgettable first impression.
im looking for the wow factor.
Front should have the basics info (attached on the picture of current business card)
i would like to add picture of myself somewhere
Back side
should have logo and maybe some pictures or past projects, you can download from my website ( www.lumvexholdings.com)

```html
<!DOCTYPE html>
<html lang="en">
<head>
<meta charset="utf-8">
<title>Lumvex Holdings – Business Card</title>
<link href="https://fonts.googleapis.com/css2?family=Roboto:wght@400;500;700&display=swap" rel="stylesheet">
<style>
  :root {
    --backdrop: #c3cbca;
    --card-black: #141414;
    --card-edge: #2a2a2a;
    --gold: #c9b17a;
    --gold-soft: #b8a06a;
    --gold-text: #a89466;
    --ink-on-gold: #1b1a17;
  }
  html, body {
    margin: 0;
    width: 1200px;
    height: 801px;
    overflow: hidden;
    background: var(--backdrop);
    font-family: "Roboto", Arial, sans-serif;
  }
  .canvas { position: relative; width: 1200px; height: 801px; }

  .card {
    position: absolute;
    width: 480px;
    height: 275px;
    border-radius: 20px;
    background: var(--card-black);
    box-shadow: 0 0 0 1px var(--card-edge), 0 14px 30px rgba(0,0,0,.18);
    overflow: hidden;
    color: var(--gold);
  }
  .card-front { left: 110px; top: 150px; }
  .card-back  { left: 610px; top: 390px; }

  .card-art { position: absolute; inset: 0; }

  /* Front */
  .brand-small {
    position: absolute; left: 38px; top: 34px;
    display: flex; align-items: center; gap: 7px;
    font-size: 11px; font-weight: 500; letter-spacing: 1.5px;
  }
  .brand-dot { width: 10px; height: 10px; border-radius: 50%; background: var(--gold); }
  .tagline {
    position: absolute; left: 38px; top: 66px;
    font-size: 10.5px; line-height: 1.45; color: var(--gold-text);
  }
  .person {
    position: absolute; left: 38px; top: 121px;
    color: var(--ink-on-gold);
  }
  .person-name { font-size: 17px; font-weight: 400; letter-spacing: .5px; }
  .person-name strong { font-weight: 700; }
  .person-role { font-size: 10.5px; font-weight: 700; margin-top: 1px; }

  .contacts {
    position: absolute; left: 38px; top: 180px;
    display: grid; grid-template-columns: 18px auto; column-gap: 10px; row-gap: 4px;
    font-size: 10.5px; color: var(--gold-text); line-height: 1.45;
  }
  .contacts svg { width: 11px; height: 11px; margin-top: 2px; fill: var(--gold-text); }

  .brand-large {
    position: absolute; left: 318px; top: 66px;
    font-size: 30px; font-weight: 700; line-height: 1.05; letter-spacing: 1px;
    color: var(--gold);
  }

  /* Back */
  .brand-back {
    position: absolute; left: 0; right: 0; top: 98px;
    display: flex; justify-content: center; align-items: center; gap: 12px;
    font-size: 24px; font-weight: 500; letter-spacing: 3px; color: var(--gold);
  }
  .brand-back .brand-dot { width: 16px; height: 16px; }
  .web-strip {
    position: absolute; left: 0; right: 0; top: 222px;
    text-align: center;
    font-size: 11px; letter-spacing: 4px; font-weight: 500;
    color: var(--ink-on-gold);
  }
</style>
</head>
<body>
<main class="canvas">

  <section class="card card-front" aria-label="Card front">
    <svg class="card-art" viewBox="0 0 480 275" aria-hidden="true">
      <path d="M0 118 H220 L232 130 V150 L220 162 H0 Z" fill="var(--gold)"/>
      <path d="M232 140 H305" stroke="var(--gold)" stroke-width="4" fill="none"/>
      <circle cx="310" cy="140" r="5" fill="var(--gold)"/>
    </svg>

    <div class="brand-small"><span class="brand-dot"></span>LUMVEX HOLDINGS</div>
    <p class="tagline" style="margin:0">Low voltage contractor<br>Offices in Miami, Broward and Palm Beach</p>

    <div class="person">
      <div class="person-name">REID <strong>CALLOWAY</strong></div>
      <div class="person-role">Operations Manager</div>
    </div>

    <div class="contacts">
      <svg viewBox="0 0 24 24"><path d="M6.6 10.8a15 15 0 0 0 6.6 6.6l2.2-2.2c.3-.3.7-.4 1-.2 1.1.4 2.3.6 3.6.6.6 0 1 .4 1 1V20c0 .6-.4 1-1 1A17 17 0 0 1 3 4c0-.6.4-1 1-1h3.5c.6 0 1 .4 1 1 0 1.3.2 2.5.6 3.6.1.3 0 .7-.2 1z"/></svg>
      <span>(305) 555-0147 (Miami)<br>(954) 555-0183 (Broward)<br>(561) 555-0126 (Palm Beach)</span>
      <svg viewBox="0 0 24 24"><circle cx="12" cy="12" r="9" fill="none" stroke="var(--gold-text)" stroke-width="2.5"/><path d="M3 12h18M12 3c3 3 3 15 0 18M12 3c-3 3-3 15 0 18" fill="none" stroke="var(--gold-text)" stroke-width="2"/></svg>
      <span>www.lumvexholdings.com</span>
      <svg viewBox="0 0 24 24"><path d="M2 5h20v14H2z M2 5l10 8 10-8" fill="none" stroke="var(--gold-text)" stroke-width="2.5"/></svg>
      <span>info@lumvexholdings.com</span>
    </div>

    <div class="brand-large">LUMVEX<br>HOLDINGS</div>
  </section>

  <section class="card card-back" aria-label="Card back">
    <svg class="card-art" viewBox="0 0 480 275" aria-hidden="true">
      <path d="M0 168 H390 L398 160 H480 V176 H398 L390 184 H0 Z" fill="var(--gold)"/>
      <path d="M0 216 H160 L168 210 H480 V236 H168 L160 242 H0 Z" fill="var(--gold)"/>
    </svg>
    <div class="brand-back"><span class="brand-dot"></span>LUMVEX HOLDINGS</div>
    <div class="web-strip">WWW.LUMVEXHOLDINGS.COM</div>
  </section>

</main>
</body>
</html>
```